Flyer Design

we need a flyer designing for our independent estate and letting agents based in Gosport Hampshire, our company name is Varley and Partners Gosport, our contact details are 27 Wren Lane, Gosport, Hampshire PO13 4TX, 02392 648307, email :marcia@varleyandpt.example.co.uk. Our special offer we'd like to advertise is for the year 2015 we aim to sell 100 properties and only charge £1000 no vat sellers fee for each property sold. We are also offering a free no obligation market appraisal by one of our professional assessors. The flyer must have this disclaimer added to the bottom of it: if you are currently on the market with another agent then your current terms and conditions may need to be reviewed prior to changing agency. We advertise on Homepanel and would like to see designs that use the colours lime green and navy blue. The final design should be eye catching and promote this special offer.

```html
<!DOCTYPE html>
<html lang="en">
<head>
<meta charset="utf-8">
<title>Varley and Partners – Featured Homes</title>
<link rel="stylesheet" href="https://fonts.googleapis.com/css2?family=Arimo:wght@400;700&family=Tinos&display=swap">
<style>
  :root {
    --backdrop: #452c04;
    --paper: #ffffff;
    --ink: #111111;
    --muted: #9aa5a0;
    --navy: #060d26;
    --lime: #8cc63f;
    --footer-ink: #f2f3f6;
    --footer-soft: #b9bdc9;
  }
  * { margin: 0; padding: 0; box-sizing: border-box; }
  html, body { width: 1200px; height: 1000px; overflow: hidden; }
  body { background: var(--backdrop); font-family: "Arimo", Arial, sans-serif; }
  .flyer { position: absolute; left: 252px; top: 0; width: 696px; height: 1000px; background: var(--paper); overflow: hidden; }
  .flyer-title {
    position: absolute; top: 9px; left: 0; width: 100%; text-align: center;
    font-family: "Tinos", "Times New Roman", serif; font-weight: 400; font-size: 24px; color: var(--ink);
  }
  .listing { position: absolute; left: 0; width: 696px; height: 168px; }
  .listing-photo { position: absolute; top: 0; width: 205px; height: 167px; }
  .listing-text { position: absolute; top: 1px; white-space: nowrap; }
  .photo-left .listing-photo { left: 14px; }
  .photo-left .listing-text { left: 235px; }
  .photo-right .listing-photo { left: 480px; }
  .photo-right .listing-text { left: 15px; }
  .listing-name { font-size: 16.5px; font-weight: 400; color: var(--ink); line-height: 19px; }
  .listing-address { font-size: 14.5px; color: var(--ink); line-height: 19px; }
  .listing-blurb { margin-top: 37px; font-size: 14.5px; line-height: 19px; color: var(--muted); }
  .offer-band {
    position: absolute; left: 0; top: 843px; width: 696px; height: 28px;
    background: var(--lime); color: var(--navy);
    font-size: 13.5px; line-height: 28px; text-align: center; font-weight: 700;
  }
  .footer { position: absolute; left: 0; top: 874px; width: 696px; height: 126px; background: var(--navy); color: var(--footer-ink); }
  .brand { position: absolute; left: 16px; top: 30px; }
  .brand-name { font-family: "Tinos", "Times New Roman", serif; font-size: 21px; line-height: 24px; color: var(--footer-ink); }
  .brand-tagline { font-family: "Tinos", "Times New Roman", serif; font-size: 9px; letter-spacing: 2px; margin-top: 4px; color: var(--footer-ink); }
  .contact { position: absolute; right: 14px; top: 14px; font-size: 14.5px; line-height: 20px; }
  .contact-heading { font-size: 16px; font-weight: 700; margin-bottom: 3px; }
  .contact-grid { display: grid; grid-template-columns: auto auto; column-gap: 4px; }
  .disclaimer {
    position: absolute; left: 16px; right: 14px; bottom: 5px;
    font-size: 9.5px; line-height: 12px; color: var(--footer-soft); white-space: nowrap;
  }
</style>
</head>
<body>
<main class="flyer">
  <h1 class="flyer-title">Some of Our More Featured Homes</h1>

  <article class="listing photo-left" style="top:55px">
    <div class="listing-photo" role="img" aria-label="Photo of Woolburry House, a grey stone house under a blue sky with flowering shrubs" style="background:linear-gradient(180deg,#2f54a8 0%,#6c7790 45%,#54514a 75%,#8b3b3a 100%)"></div>
    <div class="listing-text">
      <h2 class="listing-name">Woolburry House</h2>
      <p class="listing-address">1231 Almond Rd, London</p>
      <p class="listing-blurb">Lorem Ipsum has been the industry's standard dummy text ever<br>since the 1500s, when an unknown printer took a galley of type<br>and scrambled it to make a type specimen book. It has survived<br>not only five centuries, but also the leap into electronic typesetting,<br>remaining essentially unchanged.</p>
    </div>
  </article>

  <article class="listing photo-right" style="top:259px">
    <div class="listing-photo" role="img" aria-label="Photo of Lily House, a grey shingled house flying a flag at the end of a narrow brick path" style="background:linear-gradient(90deg,#3e4048 0%,#8d97ab 45%,#9aa4b6 60%,#3d3f45 100%)"></div>
    <div class="listing-text">
      <h2 class="listing-name">Lily House</h2>
      <p class="listing-address">1586 Almond Rd, London</p>
      <p class="listing-blurb">Lorem Ipsum has been the industry's standard dummy text ever<br>since the 1500s, when an unknown printer took a galley of type<br>and scrambled it to make a type specimen book. It has survived<br>not only five centuries, but also the leap into electronic typesetting,<br>remaining essentially unchanged.</p>
    </div>
  </article>

  <article class="listing photo-left" style="top:467px">
    <div class="listing-photo" role="img" aria-label="Photo of Sir Cruise House, a green Victorian house with red trim and a porch" style="background:linear-gradient(180deg,#8fb6dc 0%,#4d7f74 30%,#5d8a7d 55%,#8a2a22 80%,#3a3a2c 100%)"></div>
    <div class="listing-text">
      <h2 class="listing-name">Sir Cruise House</h2>
      <p class="listing-address">3586 Saint Rd, London</p>
      <p class="listing-blurb">Lorem Ipsum has been the industry's standard dummy text ever<br>since the 1500s, when an unknown printer took a galley of type<br>and scrambled it to make a type specimen book. It has survived<br>not only five centuries, but also the leap into electronic typesetting,<br>remaining essentially unchanged.</p>
    </div>
  </article>

  <article class="listing photo-right" style="top:669px">
    <div class="listing-photo" role="img" aria-label="Photo of Redburg House, a modern bungalow with young trees and a green lawn" style="background:linear-gradient(180deg,#2e7fe0 0%,#76b1ea 40%,#8a7a55 58%,#5fa63a 78%,#8e9296 100%)"></div>
    <div class="listing-text">
      <h2 class="listing-name">Redburg House</h2>
      <p class="listing-address">6786 Fountain Street, London</p>
      <p class="listing-blurb">Lorem Ipsum has been the industry's standard dummy text ever<br>since the 1500s, when an unknown printer took a galley of type<br>and scrambled it to make a type specimen book. It has survived<br>not only five centuries, but also the leap into electronic typesetting,<br>remaining essentially unchanged.</p>
    </div>
  </article>

  <p class="offer-band">2015: 100 homes sold for just £1000 sellers fee, no VAT &nbsp;·&nbsp; Free no-obligation market appraisal</p>

  <footer class="footer">
    <div class="brand">
      <p class="brand-name">Varley and Partners</p>
      <p class="brand-tagline">ESTATE &amp; LETTING AGENTS</p>
    </div>
    <div class="contact">
      <h3 class="contact-heading">Contact</h3>
      <div class="contact-grid">
        <span>Telephone:</span><span>02392 648307</span>
        <span>Email:</span><span>marcia@varleyandpt.example.co.uk</span>
        <span></span><span>martin@varleyandpt.example.co.uk</span>
      </div>
    </div>
    <p class="disclaimer">If you are currently on the market with another agent then your current terms and conditions may need to be reviewed prior to changing agency.</p>
  </footer>
</main>
</body>
</html>
```